Enhance the web site presence of Kolrith Global Limited

Upgrade the current web site www.kolrithpanel.com to share with the audience our current plan and future developments of our company. I have created a worksheet which shows all the pages that I like to have. The home page in English, Japanese and Chinese is hyperlinked to the various pages. Under the product, we should allow the user to select "single sided PCB or double sided PCB". The translation of the contents of the pages with Japanese is not complete but the English and Chinese are complete. You can download the briefing and photos in the dropbox files below;

https://www.sharelocker.net/sh/xk4trw92mpd3ab1/BBQm_Lp841zzPq2Rw7KtYnHjEa?dl=0

Target Market(s)

Electronic companies

Industry/Entity Type

Electronic

Coding

Coded - Design and coding required

Number of Pages Required

5+ page

Font styles to use
Sans Serif

Colors
00a990
0353a1
33b8a4

Requirements
Must have
• Get a sense of confidence on our company's integrity and capability to deliver the highest quality PCBs with the most competitive prices and best services. A sense of elegance is essential as we DON'T treat profits as the number one goal. Our number goal is to do the RIGHT things right. Having a mixture of our company photos will be appropriate.

```html
<!DOCTYPE html>
<html lang="en">
<head>
<meta charset="utf-8">
<title>Kolrith Global Limited</title>
<link href="https://fonts.googleapis.com/css2?family=Montserrat:wght@500;600;700&family=Open+Sans:wght@400;600;700&display=swap" rel="stylesheet">
<style>
:root{
  --teal:#00a990;
  --teal-soft:#33b8a4;
  --blue:#0353a1;
  --ink:#333;
  --muted:#555;
  --footer-bar:#2b2b2b;
}
*{box-sizing:border-box;margin:0;padding:0}
html,body{width:1200px;height:4286px;overflow:hidden}
body{position:relative;background:#fff;font-family:"Open Sans",Arial,sans-serif;color:var(--ink)}
.abs{position:absolute}
h1,h2,h3,.brand{font-family:"Montserrat",Arial,sans-serif}

/* header */
.site-header{left:0;top:0;width:1200px;height:143px;background:#fff}
.brand{left:120px;top:48px;font-size:44px;font-weight:700;color:var(--teal);letter-spacing:2px;display:flex;align-items:center;gap:12px}
.brand i{display:block;width:20px;height:20px;background:var(--blue)}
.tagline{left:120px;top:106px;font-size:11px;color:#444}
.top-contact{top:68px;font-size:14px;color:#333;display:flex;align-items:center;gap:8px;white-space:nowrap}
.top-contact .ic{width:22px;height:22px;border-radius:50%;background:var(--teal);display:flex;align-items:center;justify-content:center}
.lang{left:1005px;top:34px;font-size:12px;color:#333;display:flex;gap:6px;align-items:center}
.lang b{display:block;width:22px;height:13px;background:linear-gradient(#c33 0 50%,#fff 50%);border:1px solid #ccc}
.menu{left:1060px;top:72px;width:24px}
.menu span{display:block;height:3px;background:var(--teal);margin-bottom:5px}

/* hero */
.hero{left:0;top:143px;width:1200px;height:652px;background:linear-gradient(160deg,#cfd5d2 0%,#9aa59f 35%,#5f8a72 60%,#2f8a55 85%,#3b6a4c 100%)}
.hero-shade{left:0;top:143px;width:1200px;height:652px;background:rgba(0,0,0,.15)}
.hero-title{left:0;top:442px;width:1200px;text-align:center;color:#fff;font-weight:600;font-size:28px;line-height:34px;letter-spacing:.5px}
.pillars{left:290px;top:530px;width:620px;display:flex;justify-content:space-between}
.pillar{width:130px;text-align:center;color:#fff;font-size:9px;font-weight:700;line-height:12px}
.pillar svg{display:block;margin:0 auto 8px}
.hero-arrow{top:455px;width:26px;height:26px;border-radius:50%;border:2px solid #fff;color:#fff;font-size:14px;display:flex;align-items:center;justify-content:center}
.dots{left:0;top:843px;width:1200px;display:flex;justify-content:center;gap:10px}
.dots span{width:10px;height:10px;border-radius:50%;background:#555}
.dots span:first-child{background:#ccc}

/* welcome */
.welcome-title{left:120px;top:898px;font-size:22px;font-weight:500;color:#222}
.welcome-copy{left:120px;top:945px;width:610px;font-size:13.5px;line-height:17px;color:var(--muted)}
.welcome-copy p{margin-bottom:17px}
.btn{display:flex;align-items:center;justify-content:center;background:var(--teal);color:#fff;font-size:14px;font-weight:600;border-radius:6px}
.read-more{left:120px;top:1198px;width:198px;height:46px}

.contact-card{left:771px;top:857px;width:309px;height:400px;background:#fff;border:1px solid #cfcfcf;border-radius:12px;box-shadow:0 0 0 6px #f0f0f0}
.contact-card .head{position:absolute;left:6px;top:6px;right:6px;height:48px;background:var(--blue);color:#fff;font-family:"Montserrat",Arial,sans-serif;font-weight:700;font-size:19px;display:flex;align-items:center;justify-content:center;border-radius:6px 6px 0 0}
.field{position:absolute;left:14px;width:280px;height:42px;background:#eee;border:1px solid #ddd;color:#999;font-size:13px;padding:12px}
.contact-card .submit{position:absolute;left:14px;top:322px;width:280px;height:46px;letter-spacing:1px;font-family:"Montserrat",Arial,sans-serif}

/* single layer */
.single-title{left:120px;top:1320px;font-size:24px;font-weight:500;color:#222}
.single-intro{left:120px;top:1365px;width:900px;font-size:13.5px;line-height:18px;color:var(--muted);font-weight:600}
.spec-table{left:120px;top:1428px;width:574px;border-collapse:separate;border-spacing:0 4px;font-size:13px}
.spec-table th{height:58px;color:#fff;font-family:"Montserrat",Arial,sans-serif;font-size:20px;font-weight:600;text-align:left;padding-left:26px}
.spec-table th.app{background:var(--blue);width:405px}
.spec-table th.pct{background:var(--teal);border-left:4px solid #fff}
.spec-table td{height:64px;background:#f2f2f2;padding-left:26px;color:#444}
.spec-table td+td{border-left:4px solid #fff;padding-left:70px}
.photo-single{left:706px;top:1428px;width:374px;height:349px;background:linear-gradient(135deg,#d6d8d6 0%,#8fb89b 45%,#1f8a4a 75%,#c9cdca 100%)}

/* double layer band */
.band{left:0;top:1843px;width:1200px;height:500px;background:var(--teal)}
.photo-double{left:114px;top:1906px;width:480px;height:371px;border:6px solid #fff;background:linear-gradient(150deg,#e7e9e8 0%,#b9c9c1 40%,#4aa36f 70%,#dfe3e1 100%)}
.band-title{left:620px;top:1912px;width:440px;color:#fff;font-size:24px;font-weight:500;line-height:28px;letter-spacing:.5px}
.band-copy{left:620px;top:2008px;width:460px;color:#fff;font-size:13.5px;line-height:16px;font-weight:600}
.band-copy p{margin-bottom:16px}

/* customers */
.section-title{left:0;width:1200px;text-align:center;font-size:28px;font-weight:500;letter-spacing:1px;color:#222}
.section-sub{left:0;width:1200px;text-align:center;font-size:13.5px;line-height:17px;color:#444;font-weight:600}
.clients{left:120px;top:2503px;width:960px;display:grid;grid-template-columns:repeat(5,180px);grid-auto-rows:106px;gap:16px 15px}
.client{border:1px solid #e2e2e2;border-radius:14px;background:#fff;display:flex;align-items:center;justify-content:center;gap:8px;font-family:"Montserrat",Arial,sans-serif;font-weight:700;font-size:19px;color:#444;box-shadow:0 2px 4px rgba(0,0,0,.08)}
.client i{display:block;width:12px;height:12px;background:var(--teal)}
.client.blue{color:var(--blue)}
.client.red{color:#c8202a}

/* news */
.news{left:114px;top:3080px;width:972px;display:grid;grid-template-columns:472px 472px;grid-auto-rows:172px;gap:20px 28px}
.card{background:#f3f3f3;display:flex;padding:8px}
.card .pic{width:168px;height:156px;flex:none;background:linear-gradient(140deg,#d9dcd9,#7fae8f 55%,#c7ccc9)}
.card .body{padding:0 10px 0 16px;flex:1}
.card h3{font-size:19px;font-weight:500;color:#222;display:flex;justify-content:space-between;align-items:baseline}
.card h3 small{font-family:"Open Sans",Arial,sans-serif;font-size:11px;color:#555;font-weight:400}
.card .by{font-size:12px;font-weight:700;color:#333;margin:2px 0 4px}
.card p{font-size:13px;line-height:16px;color:#444}
.card .more{font-size:12px;color:#333;margin-top:2px}
.view-more{left:500px;top:3451px;width:196px;height:44px;font-family:"Montserrat",Arial,sans-serif;letter-spacing:1px;font-size:13px}

/* contact */
.form-row{left:234px;top:3668px;width:737px;display:flex;gap:30px}
.form-row .in{flex:1;height:36px;background:#f2f2f2;border:1px solid #e3e3e3;color:#888;font-size:11px;padding:9px 10px}
.form-msg{left:234px;top:3714px;width:737px;height:92px;background:#f2f2f2;border:1px solid #e3e3e3;color:#888;font-size:11px;padding:9px 10px}
.form-submit{left:500px;top:3846px;width:198px;height:44px;font-size:13px;letter-spacing:1px}

/* footer */
.site-footer{left:0;top:3957px;width:1200px;height:266px;background:var(--teal)}
.footer-brand{left:120px;top:4005px;font-family:"Montserrat",Arial,sans-serif;font-size:36px;font-weight:700;color:#fff;letter-spacing:2px;display:flex;align-items:center;gap:10px}
.footer-brand i{display:block;width:16px;height:16px;background:var(--blue)}
.footer-tag{left:120px;top:4052px;font-size:10px;color:#fff}
.foot-col{top:4000px;color:#fff;font-size:13px;line-height:17px}
.foot-col h4{font-family:"Montserrat",Arial,sans-serif;font-size:14px;font-weight:700;margin-bottom:20px}
.foot-col ul{list-style:none}
.foot-col li{margin-bottom:5px;font-weight:600}
.foot-col li:before{content:"›";margin-right:10px}
.contact-list li:before{content:none}
.contact-list li{display:flex;gap:8px}
.subscribe-input{width:188px;height:28px;background:#fff;border-radius:4px;color:#444;font-size:11px;padding:6px 8px;margin-top:10px}
.bottom-bar{left:0;top:4223px;width:1200px;height:63px;background:var(--footer-bar);color:#fff;font-size:13px;font-weight:600}
.bottom-bar .copy{position:absolute;left:120px;top:22px}
.socials{position:absolute;left:905px;top:18px;display:flex;gap:8px}
.socials span{width:26px;height:26px;border-radius:50%;background:#fff}
</style>
</head>
<body>

<header class="site-header abs"></header>
<div class="brand abs">KOLRITH <i></i></div>
<div class="tagline abs">Printed Circuit Board is our Business</div>
<div class="top-contact abs" style="left:680px"><span class="ic"><svg width="12" height="9" viewBox="0 0 12 9"><rect x=".5" y=".5" width="11" height="8" fill="none" stroke="#fff"/><path d="M.5 .5 6 5 11.5 .5" fill="none" stroke="#fff"/></svg></span>sales@kolrithpanel.com</div>
<div class="top-contact abs" style="left:895px"><span class="ic"><svg width="11" height="11" viewBox="0 0 11 11"><path d="M2 1 4 3 3 4.5C4 6.5 5 7.5 6.5 8L8 7 10 9 9 10.5C5 10.5 .5 6 .5 2Z" fill="#fff"/></svg></span>(852) 2946 1180</div>
<div class="lang abs"><b></b>Eng ▾</div>
<div class="menu abs"><span></span><span></span><span></span></div>

<div class="hero abs" role="img" aria-label="Photo of a PCB production line with conveyor machines in the factory"></div>
<div class="hero-shade abs"></div>
<div class="hero-arrow abs" style="left:50px">‹</div>
<div class="hero-arrow abs" style="left:1122px">›</div>
<h1 class="hero-title abs">Our Printed Circuit Board Business is<br>commited to " Excellence"</h1>
<div class="pillars abs">
  <div class="pillar"><svg width="40" height="40" viewBox="0 0 40 40"><circle cx="20" cy="20" r="17" fill="none" stroke="#fff" stroke-width="2"/><path d="M13 21l5 5 9-11" fill="none" stroke="#fff" stroke-width="2.5"/></svg>EXCELLENCE<br>IN QUALITY</div>
  <div class="pillar"><svg width="40" height="40" viewBox="0 0 40 40"><rect x="8" y="6" width="24" height="28" fill="none" stroke="#fff" stroke-width="2"/><path d="M14 20l4 4 8-9" fill="none" stroke="#fff" stroke-width="2.5"/></svg>EXCELLENCE<br>IN SERVICES</div>
  <div class="pillar"><svg width="40" height="40" viewBox="0 0 40 40"><path d="M20 4 34 10v10c0 8-6 13-14 16C12 33 6 28 6 20V10Z" fill="none" stroke="#fff" stroke-width="2"/><path d="M14 20l4 4 8-9" fill="none" stroke="#fff" stroke-width="2.5"/></svg>EXCELLENCE<br>IN SUPPLY</div>
  <div class="pillar"><svg width="40" height="40" viewBox="0 0 40 40"><circle cx="20" cy="20" r="17" fill="none" stroke="#fff" stroke-width="2"/><path d="M20 10v11l7 4" fill="none" stroke="#fff" stroke-width="2.5"/></svg>EXCELLENCE<br>IN ON TIME DELIVERY</div>
</div>
<div class="dots abs"><span></span><span></span><span></span><span></span></div>

<section class="welcome">
  <h2 class="welcome-title abs">Welcome to Kolrith Global Limited (Kolrith)</h2>
  <div class="welcome-copy abs">
    <p>Established in 2007, Kolrith Global Limited (Kolrith) is a Hong Kong company specializingin single and double sized printed circuit boards. Its manufacturing facility is located in a self-owned facility in Tangxia, Dongguan of China which is 50 minutes from Hong Kong.</p>
    <p>Our mission is to become a premium low cost PCB supplier that fully embraces hunan, social and environmental responsibilities.</p>
    <p>Through our insatiable drive to maximize efficiency, Kolrith is becoming a highly efficient PCB factory with a capacity of 40,000 square meter a month</p>
    <p>PCB is our business and it is through continued automation and innovation that will drive our growth in the next 10 years.</p>
  </div>
  <div class="btn read-more abs">Read More</div>
</section>

<aside class="contact-card abs">
  <div class="head">CONTACT US</div>
  <div class="field" style="top:70px">Name</div>
  <div class="field" style="top:122px">Email</div>
  <div class="field" style="top:174px">Phone</div>
  <div class="field" style="top:226px;height:74px">Massage</div>
  <div class="btn submit">SUBMIT</div>
</aside>

<section class="single">
  <h2 class="single-title abs">Single Layered Printed Circuit Boards</h2>
  <p class="single-intro abs">We are offering single layered circuit boards through our own production facility in China for customers in the following industries:</p>
  <table class="spec-table abs">
    <tr><th class="app">Application</th><th class="pct">Percent%</th></tr>
    <tr><td>Household appliances</td><td>60%</td></tr>
    <tr><td>Power supply</td><td>20%</td></tr>
    <tr><td>Lighting control system</td><td>10%</td></tr>
    <tr><td>others</td><td>10%</td></tr>
  </table>
  <div class="photo-single abs" role="img" aria-label="Photo of stacked green single layered circuit board panels"></div>
</section>

<section class="multi">
  <div class="band abs"></div>
  <div class="photo-double abs" role="img" aria-label="Photo of a board processing machine loading green PCB panels"></div>
  <h2 class="band-title abs">DOUBLE LAYERED AND MULTI-LAYERED PRINTED CIRCUIT BOARDS</h2>
  <div class="band-copy abs">
    <p>We are offering two layered and multi-layered circuit boards for our customers through our strategically approved printed circuit boards manufacturers.With our own UL for double sided and multi-layered circuit boards, we work with a number of strategically approved manufacturers in delivering 100% quality guaranteed printed circuit boards for our customers.</p>
    <p>We perform comprehensive quality and environmental audit of our manufacturers on quarterly and annual basis.</p>
    <p>Technical capability of our double sided/multi layered PCBs facility</p>
  </div>
</section>

<section class="customers">
  <h2 class="section-title abs" style="top:2400px">OUR CUSTOMERS</h2>
  <p class="section-sub abs" style="top:2444px">Kolrith is embracing a philosophy of being a partner with our customers. As a result,<br>we are strategic PCB suppliers to the following world renowned companies</p>
  <div class="clients abs">
    <div class="client"><i></i>Norvane</div>
    <div class="client">Haldric</div>
    <div class="client red">TESSARO</div>
    <div class="client blue">KAVELIN</div>
    <div class="client blue"><i></i>Moldura</div>
    <div class="client red">BREVIX</div>
    <div class="client red">STANBURY</div>
    <div class="client blue">ORINDA</div>
    <div class="client">PELLUX <i></i></div>
    <div class="client">ZENTRA</div>
    <div class="client"><i></i>Quorla</div>
    <div class="client">Velmora</div>
    <div class="client blue">ARDENT</div>
    <div class="client"><i></i>Kendrel</div>
    <div class="client blue">CASMIR</div>
    <div class="client red">lumera</div>
    <div class="client blue">Halvex</div>
    <div class="client blue"><i></i>Voltiq</div>
    <div class="client blue">Trinor</div>
    <div class="client blue">SAXBY</div>
  </div>
</section>

<section class="news-section">
  <h2 class="section-title abs" style="top:3018px">NEWS</h2>
  <div class="news abs">
    <article class="card"><div class="pic" role="img" aria-label="Photo of a production line machine"></div><div class="body"><h3>LOREAM IPSUM <small>Feb 6th, 2018</small></h3><div class="by">By&nbsp; Daniel Orrow</div><p>Lorem Ipsum is simply dummy text of the printing and typesetting industry. Lorem Ipsum has been the industry's standard dummy text.</p><div class="more">Read More.... ⊙</div></div></article>
    <article class="card"><div class="pic" role="img" aria-label="Photo of a factory workstation"></div><div class="body"><h3>LOREAM IPSUM <small>Feb 9th , 2018</small></h3><div class="by">By&nbsp; Daniel Orrow</div><p>Lorem Ipsum is simply dummy text of the printing and typesetting industry. Lorem Ipsum has been the industry's standard dummy text.</p><div class="more">Read More.... ⊙</div></div></article>
    <article class="card"><div class="pic" role="img" aria-label="Photo of a board handling machine"></div><div class="body"><h3>LOREAM IPSUM <small>Feb 6th, 2018</small></h3><div class="by">By&nbsp; Daniel Orrow</div><p>Lorem Ipsum is simply dummy text of the printing and typesetting industry. Lorem Ipsum has been the industry's standard dummy text.</p><div class="more">Read More.... ⊙</div></div></article>
    <article class="card"><div class="pic" role="img" aria-label="Photo of a PCB conveyor line"></div><div class="body"><h3>LOREAM IPSUM <small>Feb 9th , 2018</small></h3><div class="by">By&nbsp; Daniel Orrow</div><p>Lorem Ipsum is simply dummy text of the printing and typesetting industry. Lorem Ipsum has been the industry's standard dummy text.</p><div class="more">Read More.... ⊙</div></div></article>
  </div>
  <div class="btn view-more abs">VIEW MORE</div>
</section>

<section class="contact-form">
  <h2 class="section-title abs" style="top:3572px">CONTACT US</h2>
  <p class="section-sub abs" style="top:3617px;font-size:12px;line-height:15px">Please fill out this quick contact form and someone<br>will be in touch with you shortly</p>
  <div class="form-row abs"><div class="in">Name*</div><div class="in">Phone*</div><div class="in">Email*</div></div>
  <div class="form-msg abs">Message</div>
  <div class="btn form-submit abs">SUBMIT</div>
</section>

<footer>
  <div class="site-footer abs"></div>
  <div class="footer-brand abs">KOLRITH <i></i></div>
  <div class="footer-tag abs">Printed Circuit Board is our Business</div>
  <div class="foot-col abs" style="left:120px;top:4075px;width:200px;font-weight:600">Lorem Ipsum is simply dummy text of the printing and typese tting industry. Lorem Ipsum has been the industry's standard.<div style="margin-top:4px">Read More ⊙</div></div>
  <div class="foot-col abs" style="left:400px"><h4>QUICK LINKS</h4><ul><li>Home</li><li>Products</li><li>Technical Capabilities</li><li>News</li><li>Contact Us</li></ul></div>
  <div class="foot-col abs contact-list" style="left:629px;width:215px"><h4>HONG KONG</h4><ul>
    <li><span>◉</span><span>Kolrith Global Limited<br>18/F Harbourline Tower 72 Kellet Road Wan Chai</span></li>
    <li><span>✆</span>Tel: +852-29461180</li>
    <li><span>▣</span>Fax: +852-29461189</li>
    <li><span>✉</span>Email: sales@kolrithpanel.com</li></ul></div>
  <div class="foot-col abs" style="left:863px;width:220px"><h4>SUBSCRIBE</h4><div style="font-weight:600">Get the latest updates and offer Lorem Ipsum is simply dummy text of the printing.</div><div class="subscribe-input">Enter Your Email</div></div>
  <div class="bottom-bar abs"><span class="copy">© 2018 KOLRITH - ALL RIGHTS RESERVED</span><div class="socials"><span></span><span></span><span></span><span></span><span></span><span></span></div></div>
</footer>

</body>
</html>
```